Harbourline Panels Brochure

Harbourline Panels New Brochure Brief
Harbourline Panels are manufacturers of kitchen and wardrobe doors. We have 2 target markets, one is business to business and the other business to residential customers.
The main message of our business to residential is to inform them that they can give their kitchen or wardrobe a facelift by just replacing doors and save thousands of dollars by doing this partial renovation. However, this is in direct conflict with our business to business customers (kitchen and wardrobe companies) who buy doors from us and sell complete new kitchens and built in wardrobes to the same residential customers.
Please find links to the Harbourline Panels brochure and website below for your reference. The current dimensions of the brochure is approx. 21cmH x 29.7cmW. https://harbourlinepanels.com.au/harbourlinepanelsbrochure-2/ https://harbourlinepanels.com.au/
I would like to keep the layout of the brochure internal pages consistent with the current design, however, I am open to your ideas. The orange colour as seen on the front page should be a dominant theme as it’s based on our logo however not too overpowering, I prefer to cover to be white. I would like a new front page design, changing the door photos (they will be shades of white, not coloured) and also delete the words ‘ultimate door collection’. Heading to be along the lines of “Custom made kitchen and wardrobe doors”.
On the internal pages, some new door designs will be added and some deleted. s. We are thinking of changing all the door colours to shades of white but also stating that Harbourline Panels can colour match to any major Australian paint brand.
I would like to include a page for Wardrobe Doors with some photos, text and layout options (photo attached). Please add in the before and after images. Please create a before and after using Rob's kitchen in same layout as wardrobe before and after. Please ensure oven is cut from after image. Please add in the photos attached in this brief.
We would also like to include a FAQs section. Some more text describing our product, such as raw material, thickness of doors, painted or unpainted finish and delivery information is to be added.
Re: the ‘edges’ top of page 3; some will be deleted and one new type of edge will be added.
From page 4 onwards, there are different shapes at the bottom of each door design. We are looking for a new way to communicate this as at the moment it is taking up too much room and people do not readily understand that these door patterns can be supplied in the shapes shown in the little diagrams below them.
Please keep in mind all this information will be given at the time of design. I would like to possibly keep the brochure at 8 pages (as it is now). There may be some other changes along the way as this is still in the preliminary stage. Please include the image of our showroom in the brochure mock up.
I look forward to your reply.
Kind Regards,
Greta
* Please note, the images attach with the individual doors need to be changed to some neutral shades such as white, off white, grey, cream etc (similar to the website: https://harbourlinepanels.com.au/kitchen-doors/)

```html
<!DOCTYPE html>
<html lang="en">
<head>
<meta charset="utf-8">
<title>Harbourline Panels – Brochure Cover</title>
<link rel="stylesheet" href="https://fonts.googleapis.com/css2?family=Montserrat:wght@300;700;800&display=swap">
<style>
  :root {
    --paper: #ffffff;
    --ink: #111111;
    --ink-soft: #3a3a3a;
    --brand-orange: #f2a65a;
    --photo-light: #e6e3df;
    --photo-cabinet: #d9d5cf;
    --photo-mid: #a9a39c;
    --photo-steel: #7f7a75;
    --photo-dark: #5a5450;
    --counter-red: #8a2a1c;
    --cabinet-white: #ecebe8;
  }
  * { box-sizing: border-box; margin: 0; padding: 0; }
  html, body {
    width: 934px;
    height: 1200px;
    overflow: hidden;
    background: var(--paper);
  }
  .cover {
    position: relative;
    width: 934px;
    height: 1200px;
    background: var(--paper);
    font-family: "Montserrat", Arial, sans-serif;
    color: var(--ink);
  }
  .cover__photo {
    position: absolute;
    left: 0;
    top: 0;
    width: 663px;
    height: 1200px;
    background: linear-gradient(180deg,
      var(--photo-light) 0%,
      var(--photo-cabinet) 28%,
      var(--photo-mid) 40%,
      var(--photo-dark) 52%,
      var(--photo-steel) 62%,
      var(--photo-mid) 70%,
      var(--counter-red) 74%,
      var(--counter-red) 77%,
      var(--cabinet-white) 80%,
      var(--paper) 100%);
  }
  .cover__heading {
    position: absolute;
    left: 56px;
    top: 72px;
    font-weight: 800;
    font-size: 46px;
    line-height: 1.22;
    letter-spacing: -0.5px;
    color: var(--ink);
  }
  .cover__tagline {
    position: absolute;
    left: 56px;
    top: 1070px;
    font-weight: 300;
    font-size: 40px;
    color: var(--ink-soft);
  }
  .cover__strip {
    position: absolute;
    left: 663px;
    top: 0;
    width: 271px;
    height: 1200px;
    background: var(--paper);
  }
  .brand {
    position: absolute;
    left: 32px;
    top: 860px;
    width: 215px;
  }
  .brand__mark {
    display: block;
    width: 40px;
    height: 40px;
    background: var(--brand-orange);
    margin-bottom: 16px;
  }
  .brand__name {
    font-weight: 800;
    font-size: 30px;
    line-height: 1.15;
    color: var(--ink);
  }
</style>
</head>
<body>
  <main class="cover">
    <div class="cover__photo" role="img" aria-label="Photograph of a white kitchen with wall cabinets, a stainless rangehood, hanging utensils, a red benchtop and white lower cabinets"></div>
    <h1 class="cover__heading">Custom made kitchen<br>and wardrobe doors</h1>
    <p class="cover__tagline">Save time and money</p>
    <aside class="cover__strip">
      <div class="brand">
        <span class="brand__mark"></span>
        <p class="brand__name">Harbourline<br>Panels</p>
      </div>
    </aside>
  </main>
</body>
</html>
```